Label design for Cargo Pants.

We need modern packaging design for men's cargo pant for a brand name Talvo. All kinds of packaging designs are welcome.

The pant is folded and packaged in a poly bag. We require a label design for the brand name Talvo. The main label will be attached by a string on the belt loop. the size of that label will 25cm in length and 10cm wide. This is the first label the customer see's when he picks up the garment. Therefore, we require an eye catching design for that. If required it could have certain information about the chino pant on the main label such as Comfort fit, Wrinkle-resistant, machine washable, luxury fabric. But, if you feel that adding the above information spoils the design of the label then it is not a must to include the above information. On the back of the label we like to include the information that this pant was manufactured in an Vesk Summit certified green plant and hence the damage to the environment because of the plant is nill.

The second label is attached on to the waist band and the purpose of that label is to include the size of the pant such 32x32. The size of that label is 8cm in length and 4cm in width. There is no design on the back on this label it has to be blank.

Sample, is provided for what we use for our chino pant.

```html
<!DOCTYPE html>
<html lang="en">
<head>
<meta charset="utf-8">
<title>Talvo Cargo Pant Label – Back</title>
<link rel="stylesheet" href="https://fonts.googleapis.com/css2?family=Quicksand:wght@700&display=swap">
<style>
  :root {
    --burlap-light: #948678;
    --burlap-mid: #8a7c70;
    --burlap-dark: #7d7065;
    --edge-shade: #6f635a;
    --copy-orange: #d9822b;
    --brand-brown: #4a2d16;
  }

  html, body {
    margin: 0;
    padding: 0;
    width: 1200px;
    height: 3000px;
    overflow: hidden;
  }

  .label-back {
    position: relative;
    width: 1200px;
    height: 3000px;
    overflow: hidden;
    background: radial-gradient(ellipse at 50% 45%, var(--burlap-light) 0%, var(--burlap-mid) 60%, var(--burlap-dark) 100%);
    box-shadow: inset 0 0 40px var(--edge-shade);
  }

  .fabric-texture {
    position: absolute;
    inset: 0;
    width: 100%;
    height: 100%;
  }

  .eco-statement {
    position: absolute;
    left: 155px;
    top: 448px;
    margin: 0;
    font-family: "Quicksand", sans-serif;
    font-weight: 700;
    font-size: 76px;
    line-height: 120px;
    letter-spacing: 1px;
    color: var(--copy-orange);
  }

  .eco-statement span {
    display: block;
    white-space: nowrap;
  }

  .brand-name {
    position: absolute;
    left: 612px;
    top: 2275px;
    margin: 0;
    transform: translate(-50%, -50%) rotate(-68deg);
    font-family: "Quicksand", sans-serif;
    font-weight: 700;
    font-size: 220px;
    line-height: 1;
    letter-spacing: 6px;
    text-transform: uppercase;
    color: var(--brand-brown);
    white-space: nowrap;
  }
</style>
</head>
<body>
  <main class="label-back">
    <svg class="fabric-texture" viewBox="0 0 1200 3000" role="img" aria-label="Woven burlap fabric texture in warm grey-brown tones" preserveAspectRatio="none">
      <defs>
        <linearGradient id="burlapTone" x1="0" y1="0" x2="0" y2="1">
          <stop offset="0" stop-color="#8e8074" stop-opacity="0.35"/>
          <stop offset="0.5" stop-color="#968879" stop-opacity="0.15"/>
          <stop offset="1" stop-color="#7f7267" stop-opacity="0.35"/>
        </linearGradient>
      </defs>
      <rect width="1200" height="3000" fill="url(#burlapTone)"/>
    </svg>

    <p class="eco-statement">
      <span>Manufactured in a</span>
      <span>Vesk Summit</span>
      <span>certified</span>
      <span>green plant</span>
      <span>and hence</span>
      <span>the damage to</span>
      <span>the environment</span>
      <span>because</span>
      <span>of the plant is nill.</span>
    </p>

    <h1 class="brand-name">Talvo</h1>
  </main>
</body>
</html>
```